Slide Template Design - For Professional Powerpoint Presentation

Hello, this competition is to design one or more PowerPoint slides using the template provided as a base.

This presentation will be used by my business - to provide REPORTS (with lots of content on each slide) on investments to clients.

It is possible to win this competition by just designing 1 slide - the "Typical Slide (with Text)" is the most important.

The slides I would like are:
- Cover Page Template
- Table of Contents Template
- Section Divider Template
- Typical Slide (with Text)

The presentation should look clean, clear, highly professional, and use mainly black, grey, white colours. One colour may (but does not have to) feature as a design element.

The design is what I am most interested in - the text can be pasted in.

I do not need a logo (I already have on in black and white).

```html
<!DOCTYPE html>
<html lang="en">
<head>
<meta charset="utf-8">
<title>Slide Template Set</title>
<link rel="stylesheet" href="https://fonts.googleapis.com/css2?family=Abril+Fatface&family=Carlito:wght@400;700&family=Montserrat:wght@600&family=Prata&family=Roboto:wght@400;500;700&display=swap">
<style>
  :root {
    --ink: #000000;
    --dark-box: rgba(20, 20, 20, 0.82);
    --white: #ffffff;
    --paper: #ffffff;
    --stone: #d9d9d9;
    --stone-mid: #c9c9c9;
    --blush: #f3e8e8;
    --text-dark: #221a1a;
    --hairline: rgba(255, 255, 255, 0.75);
  }
  * { box-sizing: border-box; margin: 0; padding: 0; }
  html, body { width: 1029px; height: 1200px; overflow: hidden; background: var(--paper); }
  .canvas { position: relative; width: 1029px; height: 1200px; overflow: hidden; background: var(--paper); }
  .abs { position: absolute; }
  .slide { position: absolute; overflow: hidden; }

  /* Cover A: photo background */
  .cover-photo { left: 0; top: 0; width: 497px; height: 371px; }
  .cover-photo .photo-bg { inset: 0; background: linear-gradient(120deg, #d8d9d9 0%, #bfc1c2 40%, #8e9194 70%, #d5d6d6 100%); }
  .cover-photo .rule-v { left: 74px; top: 0; width: 1px; height: 371px; background: var(--hairline); }
  .cover-photo .rule-h { left: 0; top: 323px; width: 497px; height: 1px; background: var(--hairline); }
  .dark-box { background: var(--dark-box); color: var(--white); display: flex; flex-direction: column; align-items: center; justify-content: center; text-align: center; }
  .logo-slot { font-family: "Carlito", "Calibri", sans-serif; line-height: 1.1; }
  .logo-slot .small { font-size: 11px; }
  .logo-slot .big { font-size: 18px; font-weight: 700; }
  .cover-photo .logo-slot { left: 169px; top: 15px; width: 157px; height: 64px; }
  .cover-photo .title { left: 169px; top: 89px; width: 226px; height: 88px; font-family: "Abril Fatface", serif; font-size: 24px; line-height: 1.3; }
  .cover-photo .desc { left: 169px; top: 186px; width: 226px; height: 88px; font-family: "Prata", serif; font-size: 17px; line-height: 1.4; }
  .cover-photo .date { left: 75px; top: 100px; transform: translate(-50%, -50%) rotate(-90deg); font-family: "Montserrat", sans-serif; font-size: 12px; letter-spacing: 2px; color: #333; white-space: nowrap; }
  .cover-photo .tagline { left: 197px; top: 309px; width: 260px; height: 26px; border: 1px solid var(--hairline); display: flex; align-items: center; justify-content: center; font-family: "Montserrat", sans-serif; font-size: 9.5px; letter-spacing: 1px; color: #2a2a2a; }

  /* Cover B: black column */
  .cover-column { left: 529px; top: 0; width: 496px; height: 371px; background: var(--white); }
  .cover-column .column { left: 0; top: 0; width: 198px; height: 371px; background: var(--ink); }
  .cover-column .grey-plate { left: 111px; top: 46px; width: 151px; height: 157px; background: var(--stone); }
  .cover-column .photo { left: 80px; top: 72px; width: 158px; height: 154px; background: linear-gradient(135deg, #e6e6e6 0%, #b9bbbc 55%, #6c6f72 100%); }
  .cover-column .date { left: 46px; top: 235px; transform: translate(-50%, -50%) rotate(90deg); font-family: "Prata", serif; font-size: 11px; letter-spacing: 3px; color: var(--white); white-space: nowrap; }
  .cover-column .logo-slot { left: 263px; top: 15px; width: 136px; height: 56px; background: var(--ink); }
  .cover-column .logo-slot .big { font-size: 15px; }
  .cover-column .logo-slot .small { font-size: 10px; }
  .cover-column .title, .cover-column .desc { background: var(--ink); font-family: "Prata", serif; font-size: 17px; line-height: 1.4; }
  .cover-column .title { left: 263px; top: 103px; width: 184px; height: 80px; }
  .cover-column .desc { left: 263px; top: 187px; width: 184px; height: 104px; }
  .cover-column .edge-bar { left: 472px; top: 0; width: 20px; height: 371px; background: var(--ink); }
  .cover-column .tagline { left: 237px; top: 353px; font-family: "Abril Fatface", serif; font-size: 11px; color: var(--ink); white-space: nowrap; }

  /* Cover C: grey with architecture photo */
  .cover-grey { left: 143px; top: 389px; width: 695px; height: 384px; background: var(--stone); }
  .cover-grey .bar { left: 42px; top: 0; width: 8px; height: 152px; background: var(--ink); }
  .cover-grey .date { left: 47px; top: 211px; transform: translate(-50%, -50%) rotate(-90deg); font-family: "Roboto", sans-serif; font-weight: 700; font-size: 13px; letter-spacing: 1.5px; color: #222; }
  .cover-grey .photo { left: 86px; top: 0; width: 193px; height: 384px; background: linear-gradient(160deg, #ebe4d2 0%, #cfc7b3 35%, #5b5750 60%, #1d1b18 100%); }
  .cover-grey .logo-slot { left: 375px; top: 20px; width: 194px; height: 80px; background: var(--ink); color: var(--white); }
  .cover-grey .logo-slot .big { font-size: 21px; }
  .cover-grey .logo-slot .small { font-size: 13px; }
  .cover-grey .frame { left: 306px; top: 145px; width: 335px; height: 152px; border: 2px solid #222; display: flex; flex-direction: column; align-items: center; justify-content: center; gap: 16px; font-family: "Roboto", sans-serif; font-weight: 700; color: var(--text-dark); }
  .cover-grey .frame .title { font-size: 26px; }
  .cover-grey .frame .desc { font-size: 21px; }
  .cover-grey .block { left: 646px; top: 234px; width: 49px; height: 46px; background: var(--ink); }
  .tick { width: 2px; background: #222; }
  .cover-grey .tick-1 { left: 668px; top: 102px; height: 27px; }
  .cover-grey .tick-2 { left: 668px; top: 156px; height: 26px; }
  .cover-grey .tagline { left: 0; right: 0; margin-left: 279px; width: 416px; top: 336px; text-align: center; font-family: "Roboto", sans-serif; font-size: 18px; letter-spacing: 0.8px; color: #222; }

  /* Section divider */
  .section-divider { left: 103px; top: 798px; width: 786px; height: 402px; background: var(--blush); }
  .section-divider .photo-top { left: 23px; top: 0; width: 170px; height: 217px; background: linear-gradient(135deg, #f4f4f4 0%, #cfcfcf 50%, #8e8e8e 100%); }
  .section-divider .photo-bottom { left: 23px; top: 223px; width: 170px; height: 179px; background: linear-gradient(180deg, #d9d9d9 0%, #a9a9a9 45%, #ededed 100%); }
  .section-divider .frame { left: 480px; top: 48px; width: 233px; height: 380px; border: 2px solid #222; }
  .section-divider .label { left: 480px; top: 48px; width: 233px; height: 304px; display: flex; flex-direction: column; align-items: center; justify-content: center; font-family: "Roboto", sans-serif; font-weight: 700; font-size: 40px; line-height: 1.1; color: var(--text-dark); text-align: center; }
  .section-divider .tick-1 { left: 759px; top: 116px; height: 32px; }
  .section-divider .tick-2 { left: 759px; top: 179px; height: 31px; }
  .section-divider .foot-bar { left: 750px; top: 351px; width: 9px; height: 51px; background: var(--ink); }
</style>
</head>
<body>
<main class="canvas">

  <section class="slide cover-photo" aria-label="Cover slide with photo background">
    <div class="abs photo-bg" role="img" aria-label="Photo of hands holding a phone at a white desk with a coffee cup"></div>
    <div class="abs rule-v"></div>
    <div class="abs rule-h"></div>
    <div class="abs date">14 / 10 / 2019</div>
    <div class="abs dark-box logo-slot"><span class="small">Logo</span><span class="big">(do not design)</span><span class="small">Pty Ltd</span></div>
    <h1 class="abs dark-box title">Presentation<br>Title</h1>
    <p class="abs dark-box desc">Presentation<br>Description</p>
    <div class="abs tagline">COMPANY TAG LINE GOES HEARC</div>
  </section>

  <section class="slide cover-column" aria-label="Cover slide with black column">
    <div class="abs column"></div>
    <div class="abs grey-plate"></div>
    <svg class="abs" style="left:0;top:0" width="496" height="371" aria-hidden="true">
      <rect x="61.5" y="37.5" width="47" height="46" fill="none" stroke="#bbbbbb" stroke-width="1"/>
      <rect x="15.5" y="327.5" width="31" height="30" fill="none" stroke="#bbbbbb" stroke-width="1"/>
      <rect x="36" y="323" width="19" height="20" fill="#ffffff"/>
      <path d="M433 334.5 H472 M433.5 334 V371" stroke="#000" stroke-width="1.5" fill="none"/>
    </svg>
    <div class="abs photo" role="img" aria-label="Photo of hands holding a phone at a desk"></div>
    <svg class="abs" style="left:0;top:0" width="200" height="100" aria-hidden="true">
      <rect x="98" y="46" width="20" height="18" fill="#ffffff"/>
    </svg>
    <div class="abs date">14 / 10 / 2019</div>
    <div class="abs dark-box logo-slot"><span class="small">Logo</span><span class="big">(do not design)</span><span class="small">Pty Ltd</span></div>
    <h2 class="abs dark-box title">Presentation<br>Title</h2>
    <p class="abs dark-box desc">Presentation<br>Description</p>
    <div class="abs edge-bar"></div>
    <div class="abs tagline">COMPANY TAG LINE GOES HEAR</div>
  </section>

  <section class="slide cover-grey" aria-label="Cover slide in grey">
    <div class="abs bar"></div>
    <div class="abs date">DATE</div>
    <div class="abs photo" role="img" aria-label="Photo of a dark window frame against a pale sky"></div>
    <div class="abs dark-box logo-slot"><span class="small">Logo</span><span class="big">(do not design)</span><span class="small">Pty Ltd</span></div>
    <div class="abs tick tick-1"></div>
    <div class="abs tick tick-2"></div>
    <div class="abs frame">
      <h2 class="title">Presentation Title</h2>
      <p class="desc">Presentation Description</p>
    </div>
    <div class="abs block"></div>
    <p class="abs tagline">“Company tag line goes hear”</p>
  </section>

  <section class="slide section-divider" aria-label="Section divider slide">
    <div class="abs photo-top" role="img" aria-label="Photo of curved white architectural ribs"></div>
    <div class="abs photo-bottom" role="img" aria-label="Photo of a white interior with a curved ceiling opening"></div>
    <div class="abs frame"></div>
    <h2 class="abs label">SECTION<br>1</h2>
    <div class="abs tick tick-1"></div>
    <div class="abs tick tick-2"></div>
    <div class="abs foot-bar"></div>
  </section>

</main>
</body>
</html>
```